Personal coach needs brochure design for inspirational essay about authenticity

Overview:
I want a beautiful brochure, 11”x17” that folds to 8-1/2”x11” with 4 pages. Think of it as an oversize greeting card.
• Front cover: photograph of a dancer and title with attribution of quote (Lumafold jpeg photo attached)
• Inside spread: Copy (Helena Brisk copy attached) with some appropriate illustration, based on cover photo
• Back cover: contact information, brief descriptive copy, two small photos (jpeg photo attached; see copy for direction)
Copy for front cover title, inside spread and back cover is attached in doc titled "Helena Brisk copy"

Purpose of brochure:
I'm a personal coach and once a year I produce a 4-page illustrated inspirational essay, which invites personal reflection on living a more mindful, meaningful life. Most people I send them to collect them. Someday in the future I'd like to put a collection of these essays into a coffee table book and also create a website for the collection, which is related to the personal coaching that I do.
I have the brochures printed hard copy. I have attached a few examples from previous years. Each has a unique design related to its theme.

Concept:
This year’s essay theme, “There will only ever be one you!” is based on a quote by Helena Brisk, a famous modern dancer. The complete quote, which appears in the copy, is about being true to one’s authentic self. The essay is not about dance, but because the author of the quote was a dancer who personified this theme of being unique to self, I have selected a photo of dance for the cover.

Design Guidance:
Front cover: One possibility is to expand the background color of the Lumafold photo so the photo seems to emerge from the background. But I am open to ideas. I think the photo is artsy enough as it is, but there may be other ways to treat it (e.g. special effects) that would also work. The title should appear somewhere. Make the attribution (--Helena Brisk) in smaller type than the title.

Inside Spread: There may be ways to borrow a design motif from the cover photo to make the inside spread more visually interesting, i.e., not just straight copy. I think it may be helpful to make the font size of the quote larger than the rest of the copy, but it has to be read in sequence. Or maybe it's printed in same size as copy, but then also repeated and displayed by itself in larger type.

Back cover: If you look at some of the other examples I’ve sent, you’ll see how the back cover is typically handled. I want a reduced version of the cover to be placed near the line that says "this is the 16th in a series.." Then, there’s a jpeg photo of Helena Brisk that should be placed next to the copy description of her.

Need extra days to review

```html
<!DOCTYPE html>
<html lang="en">
<head>
<meta charset="utf-8">
<title>There Will Only Ever Be One You! – Brochure Spreads</title>
<link href="https://fonts.googleapis.com/css2?family=Cinzel:wght@400;500&family=Montserrat:ital,wght@0,300;0,400;0,600;1,600&display=swap" rel="stylesheet">
<style>
  :root {
    --backdrop: #6e6f73;
    --ink-dark: #0b0b0c;
    --panel: #1c1c1e;
    --paper-light: #ececec;
    --paper-grey: #cfcfd0;
    --title-white: #ffffff;
    --title-tan: #c9b0a1;
    --body-dark: #3a3a3c;
    --body-light: #f1f1f1;
    --serif: "Cinzel", "Trajan Pro", serif;
    --sans: "Montserrat", Arial, sans-serif;
  }
  * { box-sizing: border-box; margin: 0; padding: 0; }
  html, body { width: 939px; height: 1200px; overflow: hidden; }
  body { background: var(--backdrop); position: relative; font-family: var(--sans); }

  .spread { position: absolute; left: 76px; width: 781px; height: 505px; display: flex; }
  .spread--outer { top: 61px; }
  .spread--inner { top: 634px; }
  .page { position: relative; width: 50%; height: 100%; overflow: hidden; }

  /* ---------- Back cover ---------- */
  .back-cover { background: linear-gradient(160deg, #b9b9bb 0%, #dedede 45%, #c4c4c6 100%); }
  .back-cover__panel {
    position: absolute; left: 24px; top: 23px; width: 343px; height: 459px;
    background: var(--panel); color: var(--body-light); text-align: center;
    font-size: 5.6px; line-height: 8px; font-weight: 300;
  }
  .mini-cover {
    position: absolute; left: 143px; top: 15px; width: 57px; height: 75px;
    background: var(--ink-dark); text-align: center; overflow: hidden;
  }
  .mini-cover__title { font-family: var(--serif); font-size: 6.4px; line-height: 6.4px; color: var(--title-white); margin-top: 3px; }
  .mini-cover__title .tan { color: var(--title-tan); }
  .mini-cover__name { font-family: var(--serif); font-size: 2.6px; color: var(--title-white); }
  .mini-cover__photo { position: absolute; left: 6px; top: 23px; width: 45px; height: 38px;
    background: radial-gradient(ellipse at 55% 45%, #6d7078 0%, #32343a 55%, #121214 100%); }
  .mini-cover__sub { position: absolute; bottom: 3px; left: 2px; right: 2px; font-family: var(--serif); font-size: 2.2px; line-height: 2.6px; color: var(--title-white); }
  .back-cover__series { position: absolute; top: 99px; left: 0; right: 0; }
  .back-cover__series strong { font-weight: 600; font-size: 5.8px; display: block; margin-bottom: 1px; }
  .back-cover__contact { position: absolute; top: 121px; left: 0; right: 0; }
  .back-cover__contact p + p { margin-top: 5px; }
  .portrait {
    position: absolute; left: 117px; top: 191px; width: 109px; height: 88px;
    background: #f2f2f2; padding: 3px;
  }
  .portrait__image { width: 100%; height: 100%;
    background: radial-gradient(ellipse at 45% 60%, #9d9d9d 0%, #3d3d40 45%, #1a1a1c 100%); }
  .portrait__caption { position: absolute; top: 286px; left: 0; right: 0; }
  .about { position: absolute; left: 17px; right: 17px; text-align: justify; text-align-last: center; }
  .about strong { font-weight: 600; }
  .about--dancer { top: 308px; }
  .about--photographer { top: 376px; }

  /* ---------- Front cover ---------- */
  .front-cover { background: var(--ink-dark); text-align: center; }
  .front-cover__photo {
    position: absolute; left: 0; right: 0; top: 160px; bottom: 0;
    background:
      radial-gradient(ellipse 40% 42% at 58% 55%, #5a6474 0%, rgba(60,66,78,0.6) 45%, rgba(0,0,0,0) 100%),
      radial-gradient(ellipse 70% 55% at 50% 55%, #3b3e44 0%, #1d1e21 60%, #0b0b0c 100%);
  }
  .cover-title { position: absolute; left: 0; right: 0; font-family: var(--serif); font-weight: 400; color: var(--title-white); }
  .cover-title__line { display: block; font-size: 46px; line-height: 42px; letter-spacing: 1px; }
  .cover-title__line--tan { color: var(--title-tan); }
  .front-cover .cover-title { top: 18px; }
  .cover-attribution { display: block; font-size: 15px; line-height: 16px; letter-spacing: 1px; margin-top: -2px; }
  .front-cover__subtitle {
    position: absolute; left: 0; right: 0; top: 443px;
    font-family: var(--serif); color: var(--title-white); font-size: 12.4px; line-height: 13px; letter-spacing: 0.6px;
  }

  /* ---------- Inside spread ---------- */
  .inside-left { background: linear-gradient(150deg, #f3f3f3 0%, #e2e2e3 40%, #eeeeee 70%, #dcdcdd 100%); }
  .inside-right { background: linear-gradient(200deg, #f1f1f1 0%, #dedede 50%, #e9e9e9 100%); }
  .essay { position: absolute; left: 35px; right: 35px; top: 34px;
    font-size: 8.3px; line-height: 14.3px; font-weight: 300; color: var(--body-dark); text-align: justify; }
  .essay p + p { margin-top: 13px; }
  .quote-panel {
    position: absolute; left: 23px; top: 22px; width: 344px; height: 460px;
    background: var(--panel); color: var(--body-light);
  }
  .quote-panel__quote { position: absolute; left: 11px; right: 11px; top: 11px;
    font-size: 8.8px; line-height: 15.5px; font-weight: 600; font-style: italic; text-align: justify; }
  .quote-panel__body { position: absolute; left: 11px; right: 11px; top: 157px;
    font-size: 8.3px; line-height: 14.3px; font-weight: 300; text-align: justify; }
  .quote-panel__body p + p { margin-top: 14px; }
  .quote-panel .cover-title { top: 320px; text-align: center; }
  .quote-panel .cover-title__line { font-size: 35px; line-height: 32px; }
  .quote-panel .cover-attribution { font-size: 12px; line-height: 13px; margin-top: 0; }
</style>
</head>
<body>

<section class="spread spread--outer">
  <article class="page back-cover">
    <div class="back-cover__panel">
      <div class="mini-cover">
        <div class="mini-cover__title">There will<br><span class="tan">only ever be</span><br>one you!</div>
        <div class="mini-cover__name">Helena Brisk</div>
        <div class="mini-cover__photo" role="img" aria-label="Reduced cover photo of a dancer leaping"></div>
        <div class="mini-cover__sub">16th in a series of Labor Day essays inviting a moment of reflection</div>
      </div>
      <div class="back-cover__series">
        <strong>There Will Only Ever Be One You</strong>
        is the 16th in a series of Labor Day essays inviting a moment of reflection on living a more meaningful, more mindful life
      </div>
      <div class="back-cover__contact">
        <p>Nora Vell Adair, Ph.D.<br>Heron Hill House 12 Elm Lane<br>Ashbrook, Vermont&nbsp; 05001</p>
        <p>Mobile:&nbsp; 555-014-2290<br>Email: nvadair@brightmail.net</p>
        <p>©2023</p>
      </div>
      <div class="portrait">
        <div class="portrait__image" role="img" aria-label="Black and white photograph of Helena Brisk dancing in a flowing white dress"></div>
      </div>
      <p class="portrait__caption">“Helena Brisk in Letter to the World, No. 1”<br>© The Clara Webb Archive</p>
      <p class="about about--dancer"><strong>About Helena Brisk:</strong> Born in 1894, Helena Brisk danced and taught for over 70 years. She is recognized as a primal artistic force of the 20th century, whose influence on modernity has been compared to Dario Velt, Owen Harte, Petrov Lindt, and Anson Greer. Her themes dealt with the lives and conflicts of ordinary people, and she brought serious issues to the stage like war, poverty, intolerance and the injustices of slavery and treatment of Native Americans. Rebelling against conventions of the past, her dancing and choreography exposed the depths of human emotion through intense movements that were forceful, stark, angular, jagged, and percussive – startlingly unlike the formality of classical ballet, which she saw as antiquated</p>
      <p class="about about--photographer"><strong>About Photographer Clara Webb:</strong> In 1935 Clara Webb saw a performance by modern dancer and choreographer Helena Brisk. Webb was so inspired by the dance performance that she introduced herself to Brisk, and the two artists began an artistic collaboration that lasted more than 60 years. Webb often photographed dancers in action, to capture the emotion behind their movement. Her artistic style was in line with Brisk’s philosophy of dance. This photo from the dance, “Letter to the World,” is one of Webb’s most famous photographs. The title of this work comes from an Edith Marlowe poem, which inspired Brisk to create a dance performance based on Marlowe’s life.</p>
    </div>
  </article>

  <article class="page front-cover">
    <div class="front-cover__photo" role="img" aria-label="Dancer leaping backward in a flowing dark dress amid a cloud of dust"></div>
    <h1 class="cover-title">
      <span class="cover-title__line">There will</span>
      <span class="cover-title__line cover-title__line--tan">only ever be</span>
      <span class="cover-title__line">one you!</span>
      <span class="cover-attribution">Helena&nbsp; Brisk</span>
    </h1>
    <p class="front-cover__subtitle">16th in a series of Labor Day essays inviting<br>a moment of reflection on living a more<br>meaningful, more mindful life</p>
  </article>
</section>

<section class="spread spread--inner">
  <article class="page inside-left">
    <div class="essay">
      <p>In the rural Ohio village where I grew up, one of the highlights of Sunday morning church service -- in between congregational hymn-singing and the preacher’s sermon -- was the “special selection,” a musical performance by a parishioner. Typically, it was a vocalist or instrumental on piano, organ or violin. One Sunday, we were surprised by an unusual performance. A plump, buxom farm wife approached the pulpit, puckered up her lips and unexpectedly began to whistle the hymn “The Old Rugged Cross.” As a 10-year-old, I found this hilarious as I tried to choke back my wide-eyed amazement and giggles.</p>
      <p>Despite the irreverence of my pre-adolescent reaction, this memory has stayed with me for decades as an iconic example of the wonderment of individual differences. Of the delight I find in witnessing someone express herself in sometimes surprising and even courageous ways. Of the marvel of beholding a person be truly authentic and uniquely original.</p>
      <p>Someone who personified the irrepressible impulse to express her individuality was the early 20th century dancer and choreographer Helena Brisk. A pioneer of modern dance, she threw tradition overboard and was inspired to dance in a way that was a radical departure from the formalized style and rigidly dictated forms of classical ballet. Brisk felt compelled to express the rawness and emotion of human experience in her dancing -- not just present a form of pretty entertainment. Iconoclastically brilliant, she created a new language of dance, a revolutionary vocabulary of movement that electrified the stage, often creating a visceral response in the audience.</p>
      <p>In her biography of Brisk, her friend and equally talented choreographer Irene Solberg recalled that despite sensational reviews for her own innovative work in the Broadway musical Prairie Song!, Solberg had a gnawing feeling that her work was only mediocre. Solberg confessed her anxieties to Brisk who listened quietly and then responded, “There will only ever be one you!” Continuing, she added:</p>
    </div>
  </article>

  <article class="page inside-right">
    <div class="quote-panel">
      <p class="quote-panel__quote">“There is a vitality, a life-force, an energy, a quickening that is translated through you into action. And because there is only one of you in all of time, this expression is unique. And if you block it, the world will not have it. It is not your business to determine how good it is nor how valuable nor how it compares with other expressions. It is your business to keep it yours clearly and directly, to keep the channel open. You have to keep open and aware directly to the urges that motivate you. Above all else, keep the channel open!”</p>
      <div class="quote-panel__body">
        <p>Brisk’s wisdom reminds us that we must not hold back or judge our gifts. Although there may be moments when we doubt ourselves or when we worry that we’re not good enough, our job is to be fearless and to “keep the channel open.”</p>
        <p>Guard the precious miracle of your own uniqueness. Find that home-sweet-home feeling where you feel you are your most authentic self. There will only ever be one you! And importantly, respect the differences of others. Our world would be a drab, boring place if we all only whistled one tune.</p>
      </div>
      <h2 class="cover-title">
        <span class="cover-title__line">There will</span>
        <span class="cover-title__line cover-title__line--tan">only ever be</span>
        <span class="cover-title__line">one you!</span>
        <span class="cover-attribution">Helena&nbsp; Brisk</span>
      </h2>
    </div>
  </article>
</section>

</body>
</html>
```